Business Card Tech Company
Veradon Corp
Project: Business Card Tech Company
Business Card Tech Company -
Creative Brief
Simple
Marcel Dufresne
CEO
2745 Rue Belcourt, Québec, QC G2K 3P7, Canada
mdufresne@veradoncorp-example.com
www.veradoncorp-example.com
You can add Twitter @veradoncorp We are very open to different designs, We will provide fast feedback, You can try many styles and many fonts, Right now, our slogan is: the world made yours. You can put it on some designs if it fits well, consider we might want to change it.
We would like a back mostly visual, without much info.

```html
<!DOCTYPE html>
<html lang="en">
<head>
<meta charset="utf-8">
<title>Veradon Corp – Business Card</title>
<link href="https://fonts.googleapis.com/css2?family=Open+Sans:wght@400;600;700&display=swap" rel="stylesheet">
<style>
  :root {
    --bg: #d4d6d9;
    --card-white: #f7f7f7;
    --card-shade: #e6e6e6;
    --brand-blue: #1a73c4;
    --brand-blue-deep: #0d5aa6;
    --brand-blue-light: #3f9be0;
    --ink: #2b2b2b;
    --ink-soft: #555;
    --rule: #9a9a9a;
    --strip-grey: #d0d0d0;
  }
  * { box-sizing: border-box; margin: 0; padding: 0; }
  html, body { width: 1200px; height: 830px; overflow: hidden; }
  body {
    background: var(--bg);
    font-family: "Open Sans", Arial, sans-serif;
    position: relative;
  }
  .card {
    position: absolute;
    width: 430px;
    height: 250px;
    border-radius: 12px;
    overflow: hidden;
    box-shadow: 0 4px 10px rgba(0,0,0,.25);
  }
  .card-front {
    left: 385px; top: 190px;
    background: linear-gradient(180deg, var(--card-white) 0%, var(--card-shade) 100%);
  }
  .card-back-blue {
    left: 165px; top: 455px;
    background: radial-gradient(ellipse at 50% 45%, var(--brand-blue-light) 0%, var(--brand-blue) 45%, var(--brand-blue-deep) 100%);
  }
  .card-back-white {
    left: 610px; top: 455px;
    background: radial-gradient(ellipse at 50% 45%, #ffffff 0%, var(--card-white) 50%, var(--card-shade) 100%);
  }

  /* front */
  .brand-mark {
    position: absolute; left: 26px; top: 102px;
    display: flex; align-items: center; gap: 8px;
  }
  .brand-dot {
    width: 30px; height: 30px; border-radius: 50%;
    background: var(--brand-blue);
  }
  .brand-name {
    font-size: 26px; font-weight: 600; color: var(--brand-blue); letter-spacing: .2px;
  }
  .divider {
    position: absolute; left: 190px; top: 52px; width: 1px; height: 110px;
    background: var(--rule);
  }
  .contact {
    position: absolute; left: 200px; top: 48px; right: 16px;
    font-size: 8.5px; line-height: 1.5; color: var(--ink-soft);
    white-space: nowrap;
  }
  .contact .name { font-size: 12.5px; font-weight: 700; color: var(--ink); line-height: 1.2; }
  .contact .title { font-size: 8.5px; margin-bottom: 20px; }
  .contact .address { margin-bottom: 14px; }
  .footer-band {
    position: absolute; left: 0; right: 0; bottom: 0; height: 30px;
  }
  .footer-band svg { display: block; }
  .footer-url {
    position: absolute; right: 16px; bottom: 9px;
    font-size: 7.5px; color: #888; letter-spacing: .8px;
  }

  /* backs */
  .back-brand {
    position: absolute; inset: 0;
    display: flex; align-items: center; justify-content: center; gap: 14px;
  }
  .back-brand .brand-dot { width: 52px; height: 52px; }
  .card-back-blue .brand-dot { background: #ffffff; }
  .card-back-blue .brand-name { color: #ffffff; font-size: 40px; }
  .card-back-white .brand-name { font-size: 40px; }
</style>
</head>
<body>

  <section class="card card-front" aria-label="Business card front">
    <div class="brand-mark">
      <span class="brand-dot"></span>
      <span class="brand-name">Veradon</span>
    </div>
    <div class="divider"></div>
    <div class="contact">
      <p class="name">Marcel Dufresne</p>
      <p class="title">CEO</p>
      <p class="address">2745 Rue Belcourt, Québec, QC<br>G2K 3P7, Canada</p>
      <p>Cell: 418-555-0142</p>
      <p>Email: mdufresne@veradoncorp-example.com</p>
    </div>
    <div class="footer-band">
      <svg width="430" height="30" viewBox="0 0 430 30">
        <rect x="0" y="12" width="430" height="18" fill="var(--strip-grey)"/>
        <path d="M0 14 L230 14 L250 30 L0 30 Z" fill="var(--brand-blue)"/>
        <path d="M0 12 L232 12 L236 16 L0 16 Z" fill="var(--brand-blue-light)"/>
      </svg>
      <span class="footer-url">www.veradoncorp-example.com</span>
    </div>
  </section>

  <section class="card card-back-blue" aria-label="Business card back, blue">
    <div class="back-brand">
      <span class="brand-dot"></span>
      <span class="brand-name">Veradon</span>
    </div>
  </section>

  <section class="card card-back-white" aria-label="Business card back, white">
    <div class="back-brand">
      <span class="brand-dot"></span>
      <span class="brand-name">Veradon</span>
    </div>
  </section>

</body>
</html>
```